billboard campaign Meridale Flyers Guild

We want to run a targeted billboard campaign during the Harvest Cup in Las Vegas. The Meridale Flyers Guild is in prolonged contract negotiations with management. We want to bring public attention to our negotiations and pressure on the company to negotiate more quickly. Meridale Air owns the naming rights to "Meridale Stadium" in vegas where the harvest cup will be held. We would like artwork for this campaign that will be displayed on multiple billboards around the stadium and las vegas strip, and are seeking help in its design.
We would like to use a word play on the phrase "Big Game" which is frequently used as a alternative in advertising in reference to the Harvest Cup. Our initial thought was a simple billboard incorporating our colors and with our logo saying " Our Contract, Is Not a Big Game!" or "Meridale Flyer's Futures Are Not A Big Game!" But we are open to other suggestions and slogans. In the past we have used some artwork for picketing event which I will include for reference for logo and color scheme. The Local 4637 Haulworkers logo and union name must appear in the artwork. "Meridale Flyers Guild Haulworkers Local 4637"

Target Market(s)

Harvest Cup Attendees, Las Vegas tourists

Industry/Entity Type

aviation, labor union

Colors

Designer to choose colors to be used in the design.

Requirements
Must have
• The colors of the union logo must be those used in the included pdf art examples.

```html
<!DOCTYPE html>
<html lang="en">
<head>
<meta charset="utf-8">
<title>Meridale Flyers Guild — Not A Big Game Billboard</title>
<link rel="stylesheet" href="https://fonts.googleapis.com/css2?family=Anton&family=Montserrat:wght@600&display=swap">
<style>
  :root {
    --navy: #223a7a;
    --gold: #f2b600;
    --gold-soft: #f7c51f;
    --white: #ffffff;
    --backdrop: #e9ecef;
  }
  html, body {
    margin: 0;
    width: 1200px;
    height: 1200px;
    overflow: hidden;
    background: var(--backdrop);
  }
  .canvas {
    position: relative;
    width: 1200px;
    height: 1200px;
  }
  .billboard {
    position: absolute;
    left: 40px;
    top: 430px;
    width: 1120px;
    height: 340px;
    box-shadow: 0 10px 30px rgba(0, 0, 0, 0.18);
  }
  .billboard svg { display: block; }
  .headline-top {
    font-family: "Montserrat", sans-serif;
    font-weight: 600;
    fill: var(--navy);
  }
  .headline-main,
  .union-name,
  .union-caption {
    font-family: "Anton", sans-serif;
    fill: var(--navy);
  }
</style>
</head>
<body>
<main class="canvas">
  <section class="billboard" aria-label="Billboard: Our contract is not a big game!">
    <svg width="1120" height="340" viewBox="0 0 1120 340" xmlns="http://www.w3.org/2000/svg">
      <rect class="panel-base" width="1120" height="340" fill="var(--white)"/>

      <!-- curved navy edge and gold field -->
      <path class="field-edge" d="M203,0 C170,120 195,255 285,340 L1120,340 L1120,0 Z" fill="var(--navy)"/>
      <path class="field-gold" d="M218,0 C188,120 212,255 302,340 L1120,340 L1120,0 Z" fill="var(--gold)"/>

      <!-- faint background mark -->
      <circle class="field-mark" cx="990" cy="185" r="150" fill="var(--gold-soft)" opacity="0.6"/>

      <!-- union identity -->
      <g class="union-block">
        <circle class="union-badge" cx="105" cy="110" r="60" fill="var(--navy)"/>
        <text class="union-name" x="105" y="208" font-size="24" text-anchor="middle">HAULWORKERS</text>
        <text class="union-caption" x="105" y="268" font-size="17" text-anchor="middle" textLength="170" lengthAdjust="spacingAndGlyphs">MERIDALE FLYERS GUILD</text>
        <text class="union-caption" x="105" y="292" font-size="20" text-anchor="middle" textLength="170" lengthAdjust="spacingAndGlyphs">HAULWORKERS LOCAL 4637</text>
      </g>

      <!-- slogan -->
      <text class="headline-top" x="300" y="118" font-size="78" textLength="780" lengthAdjust="spacingAndGlyphs">OUR CONTRACT IS</text>
      <text class="headline-main" x="282" y="292" font-size="150" textLength="800" lengthAdjust="spacingAndGlyphs">NOT A BIG GAME!</text>
    </svg>
  </section>
</main>
</body>
</html>
```